Modern, profession Order Insert Card for Head Shop/Smoke shop

We are looking for a modern design for our Order Insert cards where we will have some text thanking the customer for their order.
The design needs to be professional and modern, showing our logo (SVG attached) and our website URL.
Our eCommerce store sells "head shop" items, things like bongs, rolling papers, cbd products, disposable vapes, etc.
I have uploaded 2 versions of our logo, one featuring the colour of green we use across our brand, a black logo or the logo can be inverted to be a white logo on a black background.
Target Market(s)
The websites target audience is anyone needing accessories or tools to consume medicinal marijuana/the consumers favourite herbs or any one in the vaping community.
Contact Information for Business Card
Website URL, Space for a small thank you note and our logo.
Look and feel

```html
<!DOCTYPE html>
<html lang="en">
<head>
<meta charset="utf-8">
<title>Leafline Supply – Order Insert Card</title>
<link rel="stylesheet" href="https://fonts.googleapis.com/css2?family=Arimo:wght@400;700&family=Caveat:wght@400&display=swap">
<style>
  :root {
    --brand-green: #8dbb33;
    --brand-green-light: #a4cc55;
    --card-white: #f7f7f7;
    --ink: #161616;
    --ink-soft: #2b2b2b;
    --stage: #e6e4e0;
  }
  * { box-sizing: border-box; margin: 0; padding: 0; }
  html, body { width: 1200px; height: 900px; overflow: hidden; }
  body {
    background: var(--stage);
    font-family: "Arimo", Arial, sans-serif;
    color: var(--ink);
    position: relative;
  }
  .card {
    position: absolute;
    left: 260px;
    width: 680px;
    height: 388px;
    overflow: hidden;
    box-shadow: 0 6px 18px rgba(0,0,0,0.18);
  }
  .card--front { top: 44px; background: var(--card-white); }
  .card--back { top: 468px; background: var(--brand-green); }

  .pattern-band {
    position: absolute;
    left: 0; top: 0;
    width: 100%; height: 128px;
    background: linear-gradient(180deg, var(--brand-green) 0%, var(--brand-green-light) 100%);
  }
  .pattern-field {
    position: absolute; inset: 0;
    background: radial-gradient(ellipse at 50% 50%, var(--brand-green-light) 0%, var(--brand-green) 70%);
  }

  .wordmark {
    position: absolute;
    display: flex;
    align-items: center;
    gap: 12px;
    background: #fff;
    border-radius: 40px;
    box-shadow: 0 2px 6px rgba(0,0,0,0.18);
  }
  .wordmark__dot {
    border-radius: 50%;
    background: var(--brand-green);
    flex: none;
  }
  .wordmark__name {
    font-weight: 700;
    color: var(--ink);
    white-space: nowrap;
    letter-spacing: 0.5px;
  }
  .card--front .wordmark { left: 150px; top: 100px; padding: 10px 24px 10px 12px; }
  .card--front .wordmark__dot { width: 36px; height: 36px; }
  .card--front .wordmark__name { font-size: 26px; }
  .card--back .wordmark { left: 50%; top: 50%; transform: translate(-50%,-50%); padding: 16px 36px 16px 18px; gap: 18px; }
  .card--back .wordmark__dot { width: 60px; height: 60px; }
  .card--back .wordmark__name { font-size: 44px; }

  .address {
    position: absolute;
    right: 40px; top: 150px;
    text-align: right;
    font-size: 15px;
    line-height: 1.3;
    color: var(--ink-soft);
  }
  .website {
    position: absolute;
    right: 40px; top: 232px;
    font-size: 15px;
    color: var(--ink-soft);
  }
  .person { position: absolute; left: 40px; top: 205px; }
  .person__name { font-size: 28px; font-weight: 700; color: var(--ink); }
  .person__role { font-size: 16px; color: var(--brand-green); margin-top: 2px; }
  .contact {
    position: absolute;
    left: 40px; top: 300px;
    font-size: 17px;
    line-height: 1.7;
    color: var(--ink-soft);
  }
  .thanks-note {
    position: absolute;
    right: 40px; top: 318px;
    font-family: "Caveat", cursive;
    font-size: 24px;
    color: var(--ink-soft);
  }
</style>
</head>
<body>
  <section class="card card--front" aria-label="Order insert card, front">
    <div class="pattern-band" role="img" aria-label="Pattern of line-drawn smoke shop items: pipes, hookahs, vapes, matches, tobacco packs and a top-hatted gentleman"></div>
    <div class="wordmark">
      <span class="wordmark__dot"></span>
      <span class="wordmark__name">LEAFLINE SUPPLY</span>
    </div>
    <p class="address">Leafline Supply Ltd,<br>Unit 4 Marlow Yard, 22 Ferris Lane<br>London, N7 3QP</p>
    <p class="website">www.leaflinesupply.com</p>
    <div class="person">
      <p class="person__name">Your Name Here</p>
      <p class="person__role">President/Founder</p>
    </div>
    <p class="contact">(111) 222.3333<br>hello@leaflinesupply.com</p>
    <p class="thanks-note">Thank you for your order – Note Here</p>
  </section>

  <section class="card card--back" aria-label="Order insert card, back">
    <div class="pattern-field" role="img" aria-label="Faint pattern of line-drawn smoke shop items: cigarettes, pipes, hookahs, vape mods, e-liquid bottles, matches and tobacco packs"></div>
    <div class="wordmark">
      <span class="wordmark__dot"></span>
      <span class="wordmark__name">LEAFLINE SUPPLY</span>
    </div>
  </section>
</body>
</html>
```